Box for Colorado based custom buckle and belt company

We are looking to design a box to be used to hold belts that will be delivered through Brellix's QTR program. It should have a rustic/western feel (potentially as basic as simulated mountains) and include our company's name (R&P Clasps), website (www.randpclasps.example). There needs to be a place to attach a sticker containing a SKU on the back or side of the box.

Target Market(s)

Primary customers will be men. Our products are on the more expensive side (e.g., $100-350 for a belt).

Most customers will consider themselves to be "weekend cowboys." Someone who enjoys the western ideas, but does not live then 7 days a week.

Industry/Entity Type

Clothing

Font styles to use
Serif

Requirements
Must have
• -Company Name: R&P Clasps
• -Website: www.randpclasps.example
• -Contact info: walt@randpclasps.example and (800) 555-0192
Should not have
• Overly complicated. Would prefer clean and simple.

```html
<!DOCTYPE html>
<html lang="en">
<head>
<meta charset="utf-8">
<title>R&amp;P Clasps — Belt Box</title>
<link rel="stylesheet" href="https://fonts.googleapis.com/css2?family=Cormorant+Garamond:wght@500&family=Josefin+Sans:wght@400&display=swap">
<style>
  :root {
    --backdrop: #d8cebf;
    --leather-black: #121011;
    --leather-black-soft: #1d1a1a;
    --leather-brown: #4a3021;
    --leather-brown-deep: #36231a;
    --gold: #c79a52;
    --gold-deep: #9a7035;
    --silver: #e6e2dc;
    --muted-gold: #a88a5c;
  }
  * { margin: 0; padding: 0; box-sizing: border-box; }
  html, body { width: 1200px; height: 1031px; overflow: hidden; }
  body { background: var(--backdrop); position: relative; }

  .box-face {
    position: absolute; left: 200px; top: 30px; width: 800px; height: 970px;
    background: radial-gradient(ellipse at 50% 35%, var(--leather-black-soft), var(--leather-black) 75%);
    box-shadow: 0 10px 30px rgba(0,0,0,.25);
    overflow: hidden;
  }

  .emblem-panel {
    position: absolute; left: 200px; top: 105px; width: 400px; height: 407px;
    background: radial-gradient(circle at 50% 45%, var(--leather-brown), var(--leather-brown-deep));
  }
  .emblem-ring { position: absolute; left: 0; top: 0; width: 400px; height: 407px; }

  .flourish {
    position: absolute; left: 290px; width: 220px; height: 24px;
    background: linear-gradient(90deg, transparent, var(--gold-deep) 15%, var(--gold) 50%, var(--gold-deep) 85%, transparent);
    opacity: .55;
  }
  .flourish--top { top: 600px; }
  .flourish--bottom { top: 724px; }

  .brand-name {
    position: absolute; left: 0; right: 0; top: 636px; text-align: center;
    font-family: "Cormorant Garamond", Georgia, serif; font-weight: 500;
    font-size: 64px; line-height: 80px; color: var(--silver);
  }

  .web-icon { position: absolute; left: 384px; top: 800px; width: 32px; height: 32px; }

  .website {
    position: absolute; left: 0; right: 0; top: 848px; text-align: center;
    font-family: "Josefin Sans", Arial, sans-serif; font-size: 17px;
    letter-spacing: 3.4px; color: var(--muted-gold);
  }

  .contact-band {
    position: absolute; left: 0; bottom: 0; width: 800px; height: 84px;
    background: linear-gradient(180deg, var(--leather-brown), var(--leather-brown-deep));
    display: flex; align-items: center; justify-content: center;
    font-family: "Josefin Sans", Arial, sans-serif; font-size: 17px;
    letter-spacing: 2.6px; color: var(--silver);
    padding-bottom: 14px;
  }
  .contact-band .divider { margin: 0 10px; }
</style>
</head>
<body>
  <main class="box-face">
    <div class="emblem-panel">
      <svg class="emblem-ring" viewBox="0 0 400 407" aria-hidden="true">
        <circle cx="200" cy="203" r="180" fill="none" stroke="var(--gold)" stroke-width="16"/>
      </svg>
    </div>

    <div class="flourish flourish--top" role="img" aria-label="Gold ornamental scrollwork flourish"></div>
    <h1 class="brand-name">R&amp;P Clasps</h1>
    <div class="flourish flourish--bottom" role="img" aria-label="Gold ornamental scrollwork flourish"></div>

    <svg class="web-icon" viewBox="0 0 32 32" aria-hidden="true">
      <g fill="none" stroke="var(--gold)" stroke-width="2">
        <circle cx="16" cy="16" r="13"/>
        <ellipse cx="16" cy="16" rx="6" ry="13"/>
        <line x1="3" y1="16" x2="29" y2="16"/>
        <line x1="5" y1="9.5" x2="27" y2="9.5"/>
        <line x1="5" y1="22.5" x2="27" y2="22.5"/>
      </g>
    </svg>
    <p class="website">WWW.RANDPCLASPS.EXAMPLE</p>

    <footer class="contact-band">
      <span>WALT@RANDPCLASPS.EXAMPLE</span><span class="divider">|</span><span>(800) 555-0192</span>
    </footer>
  </main>
</body>
</html>
```